OLU58 biz card & Stationery

LU58 is a personalized shopping experience brought to you, that lets you find and discover fashion goods through a collection of boutiques curated by taste-makers - celebrities, stylists, designers, and fashion bloggers. Boutiques uses visual technology to help fashionistas discover and shop their look and creates the opportunity for designers to showcase their collections and latest inspirations online.

OLU58 is built on technology developed by our team of fashion experts who work with engineers to “teach” our computer systems to understand various patterns, pairings, and genre definitions. When signed into your account, OLU58 learns about your style and preferences and in turn, provides you better results and recommendations over time. Ultimately, OLU58 will provide shoppers with a much richer and interactive shopping experience and help drive traffic to retailers' websites.

We need a definitely cool business card. The card must be black! And must use our official logo which can be download from OLU58.com

The address for Letter head and evenlop, please use 4872 Crestwick Parkway, Sutie 510 Los Angeles CA90412, email will be anyone@OLU58.com, website is www.OLU58.com

thanks

We received some of the design, thanks. But most of the design are not what we want. We need a very clean version with black ground, you may also use some dark gray to add the element. please take a look at http://morvalstudio.no/work/#pelter__ostrama/, we do like this kind of design very much. hope it help.

```html
<!DOCTYPE html>
<html lang="en">
<head>
<meta charset="utf-8">
<title>OLU58 Business Card &amp; Stationery</title>
<link rel="stylesheet" href="https://fonts.googleapis.com/css2?family=Jost:wght@300;500&display=swap">
<style>
  :root {
    --ink: #0b0b0b;
    --graphite: #3a3a3a;
    --paper: #ffffff;
    --backdrop: #e9e7e2;
    --text-dark: #1a1a1a;
    --shadow: rgba(0, 0, 0, 0.18);
  }
  * { box-sizing: border-box; margin: 0; padding: 0; }
  html, body { width: 1200px; height: 900px; overflow: hidden; }
  body { background: var(--backdrop); position: relative; font-family: "Jost", sans-serif; }

  .sheet { position: absolute; box-shadow: 0 4px 14px var(--shadow); overflow: hidden; }
  .sheet svg.shapes { position: absolute; inset: 0; width: 100%; height: 100%; display: block; }

  .brand { position: absolute; line-height: 1; }
  .brand__name { font-family: "Jost", sans-serif; font-weight: 300; letter-spacing: 0.14em; display: block; }
  .brand__tagline { font-family: "Jost", sans-serif; font-weight: 500; letter-spacing: 0.22em; display: block; text-transform: uppercase; }

  .contact { position: absolute; font-family: "Jost", sans-serif; font-weight: 300; font-style: normal; color: var(--text-dark); line-height: 1.5; }

  /* Business card front */
  .card-front { left: 40px; top: 80px; width: 250px; height: 146px; background: var(--ink); }
  .card-front .brand { left: 24px; top: 54px; color: var(--paper); }
  .card-front .brand__name { font-size: 26px; }
  .card-front .brand__tagline { font-size: 6px; margin-top: 9px; color: #bdbdbd; }

  /* Business card back */
  .card-back { left: 310px; top: 80px; width: 250px; height: 146px; background: var(--paper); }
  .card-back .contact { left: 64px; top: 42px; font-size: 8px; }

  /* Envelope */
  .envelope { left: 40px; top: 380px; width: 520px; height: 260px; background: var(--paper); }
  .envelope .brand { left: 128px; top: 132px; color: var(--ink); }
  .envelope .brand__name { font-size: 34px; }
  .envelope .brand__tagline { font-size: 6.5px; margin-top: 8px; }
  .envelope .contact { left: 346px; top: 108px; font-size: 8px; }

  /* Letterhead */
  .letterhead { left: 600px; top: 54px; width: 560px; height: 792px; background: var(--paper); }
  .letterhead .brand { left: 56px; top: 52px; color: var(--ink); }
  .letterhead .brand__name { font-size: 30px; }
  .letterhead .brand__tagline { font-size: 6.5px; margin-top: 8px; }
</style>
</head>
<body>

  <section class="sheet card-front" aria-label="Business card, front">
    <svg class="shapes" viewBox="0 0 250 146" aria-hidden="true">
      <polygon points="190,0 250,0 250,146 160,146" fill="#3a3a3a"/>
      <rect x="214" y="16" width="20" height="20" fill="#ffffff"/>
    </svg>
    <div class="brand">
      <span class="brand__name">OLU58</span>
      <span class="brand__tagline">Curated Style Boutiques</span>
    </div>
  </section>

  <section class="sheet card-back" aria-label="Business card, back">
    <address class="contact">
      4872 Crestwick Parkway, Sutie 510<br>
      Los Angeles CA90412<br>
      email: anyone@OLU58.com<br>
      www.OLU58.com
    </address>
  </section>

  <section class="sheet envelope" aria-label="Envelope">
    <svg class="shapes" viewBox="0 0 520 260" aria-hidden="true">
      <polygon points="0,0 520,0 520,36 90,36 0,110" fill="#0b0b0b"/>
      <rect x="0" y="110" width="70" height="150" fill="#3a3a3a"/>
      <rect x="26" y="150" width="18" height="18" fill="#ffffff"/>
    </svg>
    <div class="brand">
      <span class="brand__name">OLU58</span>
      <span class="brand__tagline">Curated Style Boutiques</span>
    </div>
    <address class="contact">
      4872 Crestwick Parkway, Sutie 510<br>
      Los Angeles CA90412<br>
      email: anyone@OLU58.com<br>
      www.OLU58.com
    </address>
  </section>

  <section class="sheet letterhead" aria-label="Letterhead">
    <svg class="shapes" viewBox="0 0 560 792" aria-hidden="true">
      <polygon points="470,0 560,0 560,792 520,792" fill="#0b0b0b"/>
      <polygon points="440,0 470,0 520,792 500,792" fill="#3a3a3a"/>
      <rect x="500" y="70" width="24" height="24" fill="#ffffff"/>
      <text transform="translate(546,770) rotate(-90)" font-family="Jost, sans-serif" font-weight="300" font-size="7.5" fill="#ffffff" letter-spacing="0.4">4872 Crestwick Parkway, Sutie 510 Los Angeles CA90412 · email: anyone@OLU58.com · www.OLU58.com</text>
    </svg>
    <div class="brand">
      <span class="brand__name">OLU58</span>
      <span class="brand__tagline">Curated Style Boutiques</span>
    </div>
  </section>

</body>
</html>
```